<作成物>
■リッチメッセージ
リッチメニュー
合計2枚

〈リッチメニューの項目〉
下の段左から右へ①〜③
下の段左から右へ④〜⑤

〈リッチメニューの表示名〉
①ホームページ ②メニュー   ③SNS
④お客様の声  ⑤スタッフ・店 ⑥予約

デザイン重視でここの表示名はデザイン的に英語の方がよければ
英語でも大丈夫です。意味がわかって
ニュアンスがあっていれば文字を短くするのも
お任せします。あくまでデザイン重視です。

〈画像はこちらから〉

画像
https://47.kovaload.zz/0922-ab73c1d0e5f2a4b6c8d9e0f1a2b3c4d5e6

ロゴ
https://61.kovaload.zz/0922-3d91f7a2c4b6e8d0f1a3c5e7b9d2f4a6c8

※こちらの作成以外に勝手に使用された場合は
著作権侵害で法的手段をとらせていただきます。
作成事例にもしようしないでください。

<サイズ>
・リッチメッセージ(1040×1040ピクセル)
・リッチメニュー(1200×810ピクセル)

<納品形式>
・ai形式(イラストレーターデータ)
・JPG
<詳細>
※添付ファイルをご確認ください。

<備考>
ブランディング効果を期待しています。
どんどん何個でも応募ください。

```html
<!DOCTYPE html>
<html lang="ja">
<head>
<meta charset="utf-8">
<title>プライベートエステサロン リッチメッセージ・リッチメニュー</title>
<link rel="stylesheet" href="https://fonts.googleapis.com/css2?family=Noto+Serif+JP:wght@400;500;600&family=Shippori+Mincho:wght@500;600&display=swap">
<style>
  :root{
    --page:#ffffff;
    --ink-dark:#1a1816;
    --panel:#211f1d;
    --tile:#2b2826;
    --tile-edge:#3a3632;
    --gold:#c9a46a;
    --gold-soft:#a8874f;
    --white:#ffffff;
    --photo-a:#cbb7a4;
    --photo-b:#8d7462;
    --photo-c:#4a3a30;
    --band:rgba(30,26,22,.78);
  }
  *{box-sizing:border-box;margin:0;padding:0}
  html,body{width:798px;height:1200px;overflow:hidden;background:var(--page)}
  body{position:relative;font-family:"Noto Serif JP",serif}

  /* rich message */
  .rich-message{position:absolute;left:75px;top:27px;width:650px;height:640px;background:var(--ink-dark);overflow:hidden}
  .hero-photo{position:absolute;left:0;top:0;width:650px;height:360px;
    background:linear-gradient(160deg,var(--photo-a) 0%,#b39d8a 45%,var(--photo-b) 80%,var(--photo-c) 100%)}
  .tagline{position:absolute;left:0;top:278px;width:650px;height:82px;background:var(--band);
    display:flex;align-items:center;justify-content:center;gap:8px;color:var(--white);
    font-family:"Shippori Mincho",serif}
  .tagline .main{font-size:34px;letter-spacing:2px;font-weight:500}
  .tagline .note{font-size:20px;margin-top:8px}
  .gallery{position:absolute;left:0;top:368px;width:650px;height:112px;display:flex;gap:6px;padding:0 4px}
  .gallery div{flex:1;height:100%}
  .gallery .g1{background:linear-gradient(135deg,#a88569,#5e4434)}
  .gallery .g2{background:linear-gradient(135deg,#c9b6a4,#7c6452)}
  .gallery .g3{background:linear-gradient(135deg,#b8a391,#6f5847)}
  .gallery .g4{background:linear-gradient(135deg,#5a5460,#23202a)}
  .brand-block{position:absolute;left:0;top:480px;width:650px;height:160px;display:flex;align-items:center;padding-left:26px}
  .brand-mark{width:118px;display:flex;flex-direction:column;align-items:center;gap:8px}
  .brand-mark .ring{width:66px;height:66px;border-radius:50%;border:2px solid var(--gold)}
  .brand-mark .name{color:var(--gold);font-size:15px;letter-spacing:1px}
  .brand-copy{margin-left:26px;display:flex;flex-direction:column;align-items:center;width:460px;font-family:"Shippori Mincho",serif}
  .brand-copy .lead{color:var(--white);font-size:31px;letter-spacing:1px}
  .brand-copy .rule{width:440px;height:2px;background:var(--gold);margin:12px 0 10px}
  .brand-copy .title{color:var(--gold);font-size:33px;letter-spacing:3px}

  /* rich menu */
  .rich-menu{position:absolute;left:27px;top:667px;width:744px;height:508px;background:var(--panel);
    padding:14px;display:grid;grid-template-columns:repeat(3,1fr);grid-template-rows:repeat(2,1fr);gap:12px}
  .menu-tile{position:relative;background:var(--tile);border:2px solid var(--gold-soft);
    display:flex;flex-direction:column;align-items:center;justify-content:center;gap:18px}
  .menu-tile::before{content:"";position:absolute;inset:8px;border:1px solid var(--gold-soft);opacity:.8}
  .menu-tile svg{width:86px;height:74px}
  .menu-tile .label{color:var(--white);font-size:21px;letter-spacing:1px}
</style>
</head>
<body>
  <section class="rich-message">
    <div class="hero-photo" role="img" aria-label="フェイシャルトリートメントを受ける女性の施術写真"></div>
    <div class="tagline"><span class="main">独自の技術に自信あり</span><span class="note">（特許技術）</span></div>
    <div class="gallery">
      <div class="g1" role="img" aria-label="オイルを使った施術の写真"></div>
      <div class="g2" role="img" aria-label="ボディトリートメントの写真"></div>
      <div class="g3" role="img" aria-label="リラクゼーション施術の写真"></div>
      <div class="g4" role="img" aria-label="夜の街並みの写真"></div>
    </div>
    <div class="brand-block">
      <div class="brand-mark"><span class="ring"></span><span class="name">ルミエ美容工房</span></div>
      <div class="brand-copy">
        <span class="lead">完全個室の特別空間を提供する</span>
        <span class="rule"></span>
        <span class="title">プライベートエステサロン</span>
      </div>
    </div>
  </section>

  <nav class="rich-menu">
    <div class="menu-tile">
      <svg viewBox="0 0 86 74" fill="none" stroke="#fff" stroke-width="4"><rect x="6" y="8" width="74" height="56" rx="3"/><line x1="6" y1="20" x2="80" y2="20"/><rect x="16" y="30" width="22" height="22" fill="#fff" stroke="none"/><line x1="46" y1="32" x2="70" y2="32"/><line x1="46" y1="42" x2="70" y2="42"/><line x1="46" y1="52" x2="64" y2="52"/></svg>
      <span class="label">HOME PAGE</span>
    </div>
    <div class="menu-tile">
      <svg viewBox="0 0 86 74" fill="#fff"><circle cx="43" cy="28" r="18"/><path d="M14 72c2-16 14-24 29-24s27 8 29 24z"/></svg>
      <span class="label">MENU</span>
    </div>
    <div class="menu-tile">
      <svg viewBox="0 0 86 74" fill="#fff"><rect x="2" y="26" width="22" height="22" rx="4"/><rect x="32" y="26" width="22" height="22" rx="4"/><rect x="62" y="26" width="22" height="22" rx="4"/></svg>
      <span class="label">SNS</span>
    </div>
    <div class="menu-tile">
      <svg viewBox="0 0 86 74" fill="#fff"><path d="M8 8h70v44H34L18 66V52H8z"/><g stroke="#2b2826" stroke-width="4"><line x1="20" y1="22" x2="66" y2="22"/><line x1="20" y1="32" x2="66" y2="32"/><line x1="20" y1="42" x2="54" y2="42"/></g></svg>
      <span class="label">VOICE</span>
    </div>
    <div class="menu-tile">
      <svg viewBox="0 0 86 74" fill="#fff"><circle cx="43" cy="30" r="22"/><rect x="33" y="48" width="20" height="22" rx="4"/></svg>
      <span class="label">STAFF</span>
    </div>
    <div class="menu-tile">
      <svg viewBox="0 0 86 74" fill="none" stroke="#fff" stroke-width="4"><rect x="8" y="12" width="70" height="56" rx="3"/><line x1="8" y1="26" x2="78" y2="26"/><line x1="24" y1="4" x2="24" y2="16"/><line x1="62" y1="4" x2="62" y2="16"/><g fill="#fff" stroke="none"><rect x="16" y="34" width="10" height="8"/><rect x="32" y="34" width="10" height="8"/><rect x="48" y="34" width="10" height="8"/><rect x="64" y="34" width="8" height="8"/><rect x="16" y="50" width="10" height="8"/><rect x="32" y="50" width="10" height="8"/><rect x="48" y="50" width="10" height="8"/></g></svg>
      <span class="label">RESERVE</span>
    </div>
  </nav>
</body>
</html>
```